need a Facebook marketing ad for Kordell Welding

www.kordellwelding.com is our website to look at, I need someone to design a 15-30 second ad video/sideshow for a general welding and fabrication shop, tig welding, trailer repair, build staircases, pipe welding. I don't have the media or the artistic abilities to do it. Attached is what I have, fill in the blanks and add to it.

would like to get
1-2 video ads
1-2 graphic ads
1-2 different yard signs

```html
<!DOCTYPE html>
<html lang="en">
<head>
<meta charset="utf-8">
<title>Kordell Welding – Facebook Ad 2</title>
<link href="https://fonts.googleapis.com/css2?family=Michroma&family=Montserrat:wght@700;800&family=Roboto:wght@400;700&display=swap" rel="stylesheet">
<style>
  :root{
    --red:#e2393c;
    --red-deep:#c8242b;
    --ink:#111111;
    --white:#ffffff;
    --strip:#f4f4f4;
    --frame:#3a3a3a;
    --photo-dark:#1d2230;
    --photo-blue:#2f55c9;
    --photo-glow:#dfe8ff;
  }
  *{margin:0;padding:0;box-sizing:border-box}
  html,body{width:1200px;height:1200px;overflow:hidden;background:var(--white)}
  body{position:relative;font-family:"Roboto",Arial,sans-serif;color:var(--ink)}

  .sheet-title{
    position:absolute;top:38px;left:0;width:1200px;text-align:center;
    font-family:"Michroma",sans-serif;font-size:24px;letter-spacing:4px;color:var(--ink);
    -webkit-text-stroke:0.8px var(--ink);
  }

  .ad{
    position:absolute;left:109px;top:98px;width:1010px;height:1010px;
    border:1px solid var(--frame);overflow:hidden;background:var(--white);
  }

  .hero{position:absolute;left:0;top:0;width:1010px;height:660px}

  .brand-mark{
    position:absolute;left:52px;top:140px;display:flex;align-items:center;gap:10px;
    font-family:"Montserrat",sans-serif;font-weight:800;font-size:22px;color:var(--white);
    text-transform:uppercase;letter-spacing:1px;
  }
  .brand-mark .dot{width:18px;height:18px;border-radius:50%;background:var(--red)}

  .call-box{
    position:absolute;left:749px;top:13px;width:262px;height:54px;background:var(--white);
    display:flex;align-items:center;padding-left:62px;gap:8px;
  }
  .call-box .phone-icon{width:36px;height:36px;flex:none}
  .call-box .call-text{
    font-family:"Michroma",sans-serif;font-size:11px;letter-spacing:2px;line-height:16px;color:var(--ink);
    white-space:nowrap;-webkit-text-stroke:0.4px var(--ink);
  }

  .intro{position:absolute;left:106px;top:608px;width:500px}
  .intro h1{
    font-family:"Michroma",sans-serif;font-weight:400;font-size:26px;letter-spacing:4px;
    color:var(--red);text-transform:uppercase;line-height:36px;white-space:nowrap;
    -webkit-text-stroke:1px var(--red);
  }
  .intro .tagline{font-weight:700;font-size:17.5px;margin-top:12px;line-height:22px;letter-spacing:-0.2px;white-space:nowrap}
  .intro .about{font-size:17.4px;line-height:26.7px;margin-top:10px;letter-spacing:-0.1px}

  .services{
    position:absolute;left:695px;top:464px;width:244px;height:403px;
    background:linear-gradient(180deg,#000 0%,#000 38%,#6e1a1c 65%,#f0454a 100%);
    color:var(--white);
  }
  .services .brand-mark-small{
    position:absolute;top:100px;left:0;width:100%;text-align:center;
    font-family:"Montserrat",sans-serif;font-weight:800;font-size:15px;letter-spacing:1px;text-transform:uppercase;
  }
  .services .brand-mark-small .dot{display:inline-block;width:12px;height:12px;border-radius:50%;background:var(--white);margin-right:6px;vertical-align:-1px}
  .services h2{
    position:absolute;top:176px;left:25px;white-space:nowrap;
    font-family:"Michroma",sans-serif;font-weight:400;font-size:16px;letter-spacing:2.6px;line-height:20px;
    -webkit-text-stroke:0.7px var(--white);
  }
  .services ul{position:absolute;top:206px;left:24px;list-style:none}
  .services li{
    font-family:"Montserrat",sans-serif;font-weight:700;font-size:16.5px;letter-spacing:0.6px;line-height:29px;white-space:nowrap;
  }
  .services li::before{content:"•";margin-right:7px}

  .affiliations{
    position:absolute;left:169px;top:892px;width:678px;height:60px;background:var(--strip);
    display:flex;align-items:center;justify-content:space-around;
  }
  .badge{display:block}

  .contact{
    position:absolute;left:0;top:962px;width:100%;text-align:center;white-space:nowrap;
    font-family:"Montserrat",sans-serif;font-weight:700;font-size:16.5px;letter-spacing:0.5px;
  }
  .contact .label{color:var(--red);margin-right:8px;font-weight:700}
</style>
</head>
<body>
  <div class="sheet-title">FACEBOOK AD2</div>

  <section class="ad">
    <svg class="hero" viewBox="0 0 1010 660" role="img" aria-label="Photo of a welder in a blue helmet and jacket working with bright sparks flying">
      <defs>
        <radialGradient id="sparkGlow" cx="0.6" cy="0.82" r="0.75">
          <stop offset="0" stop-color="var(--photo-glow)"/>
          <stop offset="0.3" stop-color="#7e9cf0"/>
          <stop offset="0.6" stop-color="var(--photo-blue)"/>
          <stop offset="1" stop-color="var(--photo-dark)"/>
        </radialGradient>
        <linearGradient id="redLine" x1="0" y1="0" x2="1" y2="0">
          <stop offset="0" stop-color="var(--red-deep)"/>
          <stop offset="0.75" stop-color="var(--red)"/>
          <stop offset="1" stop-color="var(--red)" stop-opacity="0"/>
        </linearGradient>
      </defs>
      <polygon points="0,0 1010,0 1010,654 0,495" fill="url(#sparkGlow)"/>
      <polygon points="0,493 600,584 600,590 0,501" fill="url(#redLine)"/>
    </svg>

    <div class="brand-mark"><span class="dot"></span>Kordell Welding</div>

    <div class="call-box">
      <svg class="phone-icon" viewBox="0 0 36 36" aria-hidden="true">
        <circle cx="18" cy="18" r="18" fill="var(--red)"/>
        <path d="M12.5 10.5c1-.8 2-.6 2.6.4l1.4 2.4c.5.9.3 1.8-.5 2.4l-1 .7c.8 2 2.3 3.6 4.3 4.5l.8-1c.6-.8 1.6-1 2.4-.5l2.4 1.4c1 .6 1.1 1.7.3 2.6l-1.2 1.3c-1 1-2.6 1.3-4 .7-4.4-1.9-7.5-5-9.3-9.4-.6-1.4-.2-3 .8-4z" fill="var(--white)"/>
      </svg>
      <div class="call-text">CALL NOW<br>615-555-0142</div>
    </div>

    <div class="intro">
      <h1>Kordell Welding</h1>
      <p class="tagline">Your Trusted Welding and Fabrication Partner in Tennessee.</p>
      <p class="about">At Kordell Welding, we are a comprehensive welding company dedicated to providing top-notch custom fabrication, welding, and metal repair services to our valued clients. With a team of skilled welding fabricators and metal workers, we deliver superior service both in our well-equipped welding shop and on-site.</p>
    </div>

    <aside class="services">
      <div class="brand-mark-small"><span class="dot"></span>Kordell Welding</div>
      <h2>OUR SERVICES</h2>
      <ul>
        <li>General Welding</li>
        <li>Fabrication Shop</li>
        <li>Tig Welding</li>
        <li>Trailer Repair</li>
        <li>Build Staircases</li>
        <li>Pipe Welding.</li>
      </ul>
    </aside>

    <div class="affiliations">
      <svg class="badge" width="150" height="40" viewBox="0 0 150 40" role="img" aria-label="Welding society membership badge"><rect x="2" y="6" width="146" height="28" rx="4" fill="#c9ccd2"/></svg>
      <svg class="badge" width="90" height="40" viewBox="0 0 90 40" role="img" aria-label="Petroleum institute certification badge"><rect x="2" y="6" width="86" height="28" rx="4" fill="#c9ccd2"/></svg>
      <svg class="badge" width="90" height="40" viewBox="0 0 90 40" role="img" aria-label="Corrosion engineers membership badge"><rect x="2" y="6" width="86" height="28" rx="4" fill="#c9ccd2"/></svg>
      <svg class="badge" width="110" height="40" viewBox="0 0 110 40" role="img" aria-label="Nondestructive testing society badge"><rect x="2" y="6" width="106" height="28" rx="4" fill="#c9ccd2"/></svg>
    </div>

    <p class="contact"><span class="label">CONTACT DETAILS</span>Cedar Bend TN, 38100 &nbsp;| &nbsp;615-555-0142 | &nbsp;info@kordellwelding.com</p>
  </section>
</body>
</html>
```